promotional flyer for Valtera Gym

we are after a double sided a5 leaflet to promote our gym, this is to go out to the general public to entice them into getting membership.

gym membership is £30 per month

it should also include the offer of - if you present this leaflet then there will be no joining fee

some of the features of the gym include

strength machines
cardio machines
functional area
sprung floor mat area

Target Market(s)

Adults 16+ who want to go to the gym and workout

Industry/Entity Type

Gym

Font styles to use
Other font styles liked:
• montserrat Regular

Requirements
Must have
• Clean on brand design
• use images supplied by us
Nice to have
• focus on an inclusive experience as the gym will be advertised to everyone
• should also use our "fitter, stronger, Healthier"

```html
<!DOCTYPE html>
<html lang="en">
<head>
<meta charset="utf-8">
<title>Valtera Gym – Membership Leaflet</title>
<link rel="stylesheet" href="https://fonts.googleapis.com/css2?family=Montserrat:ital,wght@0,400;0,500;0,600;0,700;0,800;1,500&display=swap">
<style>
  :root {
    --orange: #e8592a;
    --slate: #5c6064;
    --band: #6c7073;
    --white: #ffffff;
    --photo-dark: #26282c;
    --photo-mid: #4b4d53;
    --photo-floor: #6a6c70;
    --photo-green: #2f7a3c;
    --photo-red: #7a2a34;
  }
  * { margin: 0; padding: 0; box-sizing: border-box; }
  html, body {
    width: 846px;
    height: 1200px;
    overflow: hidden;
    background: var(--white);
  }
  .leaflet {
    position: relative;
    width: 846px;
    height: 1200px;
    overflow: hidden;
    background: var(--white);
    font-family: "Montserrat", sans-serif;
  }
  .brand {
    position: absolute;
    left: 30px;
    top: 46px;
    width: 470px;
    text-align: center;
  }
  .brand-dot {
    display: block;
    width: 104px;
    height: 104px;
    margin: 0 auto 18px;
    border-radius: 50%;
    background: var(--orange);
  }
  .brand-name {
    font-weight: 400;
    font-size: 50px;
    letter-spacing: 5px;
    color: var(--slate);
    line-height: 1;
  }
  .brand-tagline {
    margin-top: 18px;
    font-weight: 500;
    font-size: 17px;
    letter-spacing: 2.5px;
    color: var(--orange);
  }
  .opening {
    position: absolute;
    right: 46px;
    top: 44px;
    text-align: right;
  }
  .opening-title {
    font-weight: 700;
    font-size: 28px;
    letter-spacing: 1px;
    color: var(--orange);
  }
  .opening-hours {
    font-weight: 400;
    font-size: 21px;
    line-height: 1.3;
    color: var(--slate);
  }
  .artwork {
    position: absolute;
    left: 0;
    top: 0;
  }
  .offer-text {
    font-weight: 800;
    font-size: 30px;
    letter-spacing: 3px;
    fill: var(--white);
  }
  .badge-big { font-weight: 500; font-size: 44px; fill: var(--white); letter-spacing: 1px; }
  .badge-bold { font-weight: 800; font-size: 28px; fill: var(--white); }
  .badge-small { font-weight: 700; font-size: 24px; fill: var(--white); letter-spacing: 0.5px; }
  .slogan-word {
    font-weight: 500;
    font-style: italic;
    font-size: 70px;
    letter-spacing: 2px;
    fill: var(--white);
  }
</style>
</head>
<body>
<main class="leaflet">
  <svg class="artwork" width="846" height="1200" viewBox="0 0 846 1200" xmlns="http://www.w3.org/2000/svg">
    <defs>
      <clipPath id="heroClip">
        <polygon points="0,344 846,178 846,712 0,856"/>
      </clipPath>
      <linearGradient id="heroBase" x1="0" y1="0" x2="0" y2="1">
        <stop offset="0" stop-color="var(--photo-dark)"/>
        <stop offset="0.55" stop-color="var(--photo-mid)"/>
        <stop offset="1" stop-color="var(--photo-floor)"/>
      </linearGradient>
      <radialGradient id="heroGreen" cx="0.85" cy="0.62" r="0.5">
        <stop offset="0" stop-color="var(--photo-green)" stop-opacity="0.95"/>
        <stop offset="1" stop-color="var(--photo-green)" stop-opacity="0"/>
      </radialGradient>
      <radialGradient id="heroRed" cx="0.08" cy="0.35" r="0.35">
        <stop offset="0" stop-color="var(--photo-red)" stop-opacity="0.9"/>
        <stop offset="1" stop-color="var(--photo-red)" stop-opacity="0"/>
      </radialGradient>
      <radialGradient id="heroCentre" cx="0.42" cy="0.55" r="0.3">
        <stop offset="0" stop-color="#171819" stop-opacity="0.85"/>
        <stop offset="1" stop-color="#171819" stop-opacity="0"/>
      </radialGradient>
      <linearGradient id="rule" x1="0" y1="0" x2="1" y2="0">
        <stop offset="0" stop-color="#fff" stop-opacity="1"/>
        <stop offset="1" stop-color="#fff" stop-opacity="0"/>
      </linearGradient>
    </defs>

    <g class="hero-photo" role="img" aria-label="Photo of a woman smiling while training on a chest press machine, with weight stacks, racks and a green turf area behind her" clip-path="url(#heroClip)">
      <rect x="0" y="170" width="846" height="700" fill="url(#heroBase)"/>
      <rect x="0" y="170" width="846" height="700" fill="url(#heroRed)"/>
      <rect x="0" y="170" width="846" height="700" fill="url(#heroGreen)"/>
      <rect x="0" y="170" width="846" height="700" fill="url(#heroCentre)"/>
    </g>

    <polygon class="bottom-panel" points="0,905 846,762 846,1200 0,1200" fill="var(--orange)"/>

    <g class="offer-band">
      <polygon points="0,856 846,712 846,764 0,907" fill="var(--band)"/>
      <text class="offer-text" x="423" y="820" text-anchor="middle" transform="rotate(-9.6 423 810)">NO JOINING FEE WITH THIS LEAFLET</text>
    </g>

    <g class="price-badge" transform="rotate(-10 665 318)">
      <circle cx="665" cy="318" r="128" fill="var(--orange)" stroke="var(--white)" stroke-width="6"/>
      <text class="badge-big" x="665" y="288" text-anchor="middle">GYM</text>
      <text class="badge-bold" x="665" y="324" text-anchor="middle">MEMBERSHIP</text>
      <text class="badge-small" x="665" y="358" text-anchor="middle">ONLY £30</text>
      <text class="badge-small" x="665" y="388" text-anchor="middle">PER MONTH</text>
    </g>

    <g class="slogan">
      <g transform="rotate(-9.6 45 1010)">
        <text class="slogan-word" x="45" y="1010">FITTER</text>
        <rect x="45" y="1022" width="340" height="3" fill="url(#rule)"/>
      </g>
      <g transform="rotate(-9.6 215 1078)">
        <text class="slogan-word" x="215" y="1078">STRONGER</text>
        <rect x="215" y="1090" width="420" height="3" fill="url(#rule)"/>
      </g>
      <g transform="rotate(-9.6 380 1146)">
        <text class="slogan-word" x="380" y="1146">HEALTHIER</text>
        <rect x="380" y="1158" width="440" height="3" fill="url(#rule)"/>
      </g>
    </g>
  </svg>

  <header class="brand">
    <span class="brand-dot" aria-hidden="true"></span>
    <div class="brand-name">VALTERA GYM</div>
    <div class="brand-tagline">FITTER | STRONGER | HEALTHIER</div>
  </header>

  <aside class="opening">
    <div class="opening-title">OPEN 7 DAYS</div>
    <div class="opening-hours">6am-10pm Mon-Fri</div>
    <div class="opening-hours">7am-7pm Sat-Sun</div>
  </aside>
</main>
</body>
</html>
```